The Bayfield Wellness Clinic - Practice Flyer

We need a flyer that generally advertises our services. I've uploaded one old flyer as well as examples of others. I like the style of the materials made by this practice: https://www.facebook.com/PineRidgeCounselingHouse

```html
<!DOCTYPE html>
<html lang="en">
<head>
<meta charset="utf-8">
<title>The Bayfield Wellness Clinic – Practice Flyer</title>
<link href="https://fonts.googleapis.com/css2?family=Cinzel:wght@400;600&family=Cardo&family=Open+Sans:wght@400;600&display=swap" rel="stylesheet">
<style>
:root{
  --stage:#464646;
  --paper:#ffffff;
  --olive:#8f9464;
  --olive-dark:#6e7447;
  --sage:#a9bd73;
  --sage-light:#b8cb85;
  --brown:#a0652a;
  --amber:#f1c76a;
  --ink:#222222;
  --footer:#e3e3dc;
  --phone-pill:#dcdcd3;
}
*{margin:0;padding:0;box-sizing:border-box}
html,body{width:1200px;height:1200px;overflow:hidden;background:var(--stage)}
body{font-family:"Open Sans",sans-serif;color:var(--ink);position:relative}
.flyer{position:absolute;left:256px;top:95px;width:728px;height:1030px;background:var(--paper);overflow:hidden}
.abs{position:absolute}

.header{left:0;top:0;width:728px;height:120px}
.brand{left:20px;top:12px;width:390px;text-align:center;font-family:"Cinzel",serif;color:var(--olive-dark);font-weight:600}
.brand .line1{font-size:30px;line-height:34px}
.brand .line2{font-size:33px;line-height:42px;letter-spacing:1px}
.brand .line3{font-size:13px;line-height:18px}
.mark{left:574px;top:20px;width:46px;height:46px;border-radius:50%;background:var(--sage-light)}
.phone-pill{left:455px;top:66px;width:273px;height:40px;background:var(--phone-pill);border-radius:20px 0 0 20px}
.phone-icon{left:6px;top:4px;width:32px;height:32px;border-radius:50%;background:var(--olive)}
.phone-number{left:56px;top:2px;font-family:"Cardo",serif;font-size:29px;color:var(--ink);white-space:nowrap}

.hero{left:0;top:120px;width:728px;height:341px;background:linear-gradient(90deg,#9c9684 0%,#b5ad97 45%,#8e8571 70%,#a39a84 100%)}
.intro{left:84px;top:44px;width:255px;height:297px;background:var(--sage-light);border:4px solid #c7d79b;border-bottom:none;text-align:center;padding:16px 6px 0}
.intro .lead{font-weight:600;font-size:13px;line-height:18.3px;white-space:nowrap}
.intro .rule{margin:12px auto 20px;width:110px;height:1px;background:#55603a}
.intro .body{font-size:13px;line-height:19.3px;color:#2a2a2a;white-space:nowrap}

.conditions{left:0;top:461px;width:728px;height:85px;background:var(--olive);color:#f4f4ea;font-size:13px;line-height:19.5px;text-align:center;padding-top:15px;white-space:nowrap}

.lower{left:0;top:546px;width:728px;height:405px;background:linear-gradient(100deg,#e0a24b 0%,#f3c35c 30%,#f7d77a 55%,#e9b75b 80%,#d98f3a 100%)}
.lower-fade{left:0;top:0;width:728px;height:100px;background:linear-gradient(180deg,#ffffff 0%,rgba(255,255,255,.85) 70%,rgba(255,255,255,0) 100%)}
.cbt-note{left:340px;top:13px;width:370px;text-align:center;font-size:13px;line-height:19.2px;white-space:nowrap}
.treatments{left:334px;top:97px;width:380px;height:259px;background:rgba(246,214,128,.88)}
.treatments-title{left:15px;top:10px;width:352px;height:42px;background:var(--brown);color:#fbeed7;font-family:"Cinzel",serif;font-weight:400;font-size:22px;line-height:42px;text-align:center;letter-spacing:.5px}
.treatments ul{list-style:none;position:absolute;left:0;top:81px;width:380px;text-align:center;font-size:13px;line-height:19.2px}

.stripe{left:0;top:953px;width:728px;height:10px;background:linear-gradient(180deg,#e3e3dc 0 2px,var(--olive) 2px 6px,#e3e3dc 6px)}
.footer{left:0;top:963px;width:728px;height:67px;background:var(--footer)}
.clinician{left:334px;top:902px;width:380px;height:64px;background:var(--olive);color:#f4f4ea;text-align:center;padding-top:8px;z-index:2}
.clinician .name{font-size:13px;line-height:17px}
.clinician .lic{font-size:10.5px;line-height:20px;color:#1f1f1f;white-space:nowrap}
.social{top:11px;width:44px;height:44px;border-radius:50%;border:3px solid #fff}
.s1{left:74px;background:var(--olive)}
.s2{left:130px;background:var(--amber)}
.s3{left:186px;background:var(--brown)}
.website{right:22px;top:22px;font-size:19px;white-space:nowrap}
</style>
</head>
<body>
<main class="flyer">
  <header class="abs header">
    <div class="abs brand">
      <div class="line1">The Bayfield</div>
      <div class="line2">Wellness Clinic</div>
      <div class="line3">of Greater Philadelphia LLC</div>
    </div>
    <div class="abs mark"></div>
    <div class="abs phone-pill">
      <div class="abs phone-icon">
        <svg width="32" height="32" viewBox="0 0 32 32"><path d="M11 9c1-1 2-1 3 0l2 3c.5 1 .3 1.6-.4 2.2l-1 .8c.8 1.8 2.2 3.2 4 4l.8-1c.6-.7 1.3-.9 2.2-.4l3 2c1 .7 1 1.8 0 2.8l-1 1c-1.5 1.4-4 1-7-1.2-3-2.2-5.4-5-6.6-7.8C9 13 9.4 10.6 11 9z" fill="#fff"/></svg>
      </div>
      <div class="abs phone-number">(555) 014-2837</div>
    </div>
  </header>

  <section class="abs hero" role="img" aria-label="Photo of a hooded young person sitting slumped on a stone step in front of an old wooden door">
    <div class="abs intro">
      <p class="lead">The Bayfield Wellness Clinic<br>of Greater Philadelphia (BWC)<br>provides expert clinical care for<br>anxiety disorders, obsessive<br>compulsive and related disorders<br>&amp; neurodevelopmental disorders<br>in children, adolescents &amp; adults.</p>
      <div class="rule"></div>
      <p class="body">BWC proudly provides the<br>Greater Philadelphia community<br>with state-of-the-art assessment<br>and evidence-based therapy<br>for disorders including:</p>
    </div>
  </section>

  <section class="abs conditions">
    <p>Obsessive Compulsive Disorder ✦ Trichotillomania Excoriation Disorder ✦ Generalized Anxiety Disorder ✦</p>
    <p>Panic Disorder ✦ Specific Phobias ✦ Hoarding Disorder ✦ Body Dysmophic Disorder ✦</p>
    <p>Tic Disorders ✦ ADHD Learning Disorders ✦ Insomnia ✦ Social Anxiety Disorder</p>
  </section>

  <section class="abs lower" role="img" aria-label="Photo of a family walking in a golden field at sunset, a child riding on a parent's shoulders">
    <div class="abs lower-fade"></div>
    <p class="abs cbt-note">BWC clinicians are highly trained in<br><strong>Cognitive Behavioral Therapy (CBT)</strong> which includes<br>scientifically informed techniques that are tailored<br>to each client’s unique needs.</p>
    <div class="abs treatments">
      <h2 class="abs treatments-title">Treatments We Provide</h2>
      <ul>
        <li>Cognitive Behavioral Therapy (CBT)</li>
        <li>Exposure &amp; Response Prevention (E/RP)</li>
        <li>Comperehensive Behavioral (ComB)</li>
        <li>Habit Reversal Training (HRT)</li>
        <li>Cognitive Behavioral Intervention for Tics (CBIT)</li>
        <li>Acceptance &amp; Commitment Therapy (ACT)</li>
        <li>Organizational Skills Training (OST)</li>
        <li>CBT for Insomnia (CBT-I)</li>
      </ul>
    </div>
  </section>

  <div class="abs stripe"></div>
  <footer class="abs footer">
    <div class="abs social s1" aria-label="Social link"></div>
    <div class="abs social s2" aria-label="Social link"></div>
    <div class="abs social s3" aria-label="Social link"></div>
    <p class="abs website">www.BayfieldWellnessClinic.com</p>
  </footer>

  <div class="abs clinician">
    <p class="name">Elena R. Marsh, PsyD</p>
    <p class="name">Executive Director Licensed Clinical Psychologist</p>
    <p class="lic">New Jersey Lic. No. 00X00000000 - Pennsylvania Lic. No. XX0000000</p>
  </div>
</main>
</body>
</html>
```